Start up International Security Business Needs a Web Design

Based in Edinburgh UK, Verin Global Services (www.verings.example) provides security services of various types in challenging or high threat environments internationally for government and private sector organizations. We provide risk assessments, security audits and training, medical support, close protection for individuals, groups and events, crisis management, and evacuation coordination; we enable businesses to operate in challenging locations. Our experts are highly trained and qualified with exceptional experience worldwide.
The name Verin was selected in competition and derives from Greek Mythology where it was a giant man of bronze gifted by Zeus to protect Europa from invaders and pirates, circling the island of Crete three times daily (essentially establishing a protective perimeter). The centre of the current logo (inside the "O") is a stylized symbol of Zeus; we use it as a customized "bullet" on documents and acts as an abbreviated logo.
We purposefully omitted any reference to security in the name/logo and the web-page should be discreet in the same manner - we provide services of this nature but do not draw attention to ourselves. Generic images for visuals should be used as opposed to any existing stock photography we possess as a company. Imagery that relay protection, an international reach, innovation, modern vistas, varied countrysides (desert, jungle, urban settings, an old fortress?) would be seen positively.
The current colour of blue and white in the principal logo has received positive response for the clean lines, and the grey-ish scale writing similarly works. The "O" with the symbol inside has been used as customized "bullets" inside of documents, and we envisioned several other potential uses for web pages, etc.
However the integration of bronze as a third colour given the origin of Verin could be a consideration as well.
The final design should communicate clarity, an international reach in difficult areas with our broad experience and strength without being aggressive. There must be a section where the countries we have experience operating in is displayed graphically (i.e. a global map where the countries are coloured in). Countries are USA, Canada, UK, France, Bosnia, UAE, Qatar, Libya, Tunisia, Afghanistan, Iraq, Turkey, Sudan, Egypt, Central African Republic, Somalia, Rwanda, Somaliland. Additional sections should include "Our Clients", "Our Services", "Our Expertise", "Join Our Team" which should have a personal details form and ability to upload a CV, "Our Contact Details" which should also allow for submission of a web enquiry
Reason: Extension granted at the request of several designers in order to conceptualize solutions whilst initial selection process begins. Feedback on each design submitted will be provided. Very many thanks to all who took the time to share their vision for our company's website.
Verin GS
Target Market(s)
Private Sector energy, logistics, and infrastructure companies along with government organizations
Industry/Entity Type
Security
Logo Text
Verin
Number of Pages Required
3 page
Requirements
Must have
- There must be a section where the countries we have experience operating in is displayed graphically (i.e. a global map where the countries are coloured in). Countries are USA, Canada, UK, France, Bosnia, UAE, Qatar, Libya, Tunisia, Afghanistan, Iraq, Turkey, Sudan, Egypt, Central African Republic, Somalia, Rwanda, Somaliland. Additional sections should include "Our Clients", "Our Services", "Our Expertise", "Join Our Team" which should have a personal details form and ability to upload a CV, "Our Contact Details" which should also allow for submission of a web enquiry
Should not have
- Aggressive pictures of guards, weapons, etc

```html
<!DOCTYPE html>
<html lang="en">
<head>
<meta charset="utf-8">
<title>Verin Global Services</title>
<link rel="stylesheet" href="https://fonts.googleapis.com/css2?family=Montserrat:wght@600&family=Questrial&family=Open+Sans:wght@400;700&display=swap">
<style>
:root{
  --brand:#15508a;
  --brand-dark:#0f3f6e;
  --band:#165b93;
  --ink:#555a60;
  --muted:#8a8f95;
  --light:#f3f3f3;
  --field:#ececec;
  --night:#0a0b0e;
  --white:#ffffff;
}
*{margin:0;padding:0;box-sizing:border-box}
html,body{width:1200px;height:3231px;overflow:hidden;background:var(--white)}
body{font-family:"Open Sans",Arial,sans-serif;color:var(--ink);position:relative}
section,header,footer{position:relative;width:1200px}
.heading{font-family:"Questrial",Arial,sans-serif;color:var(--brand);text-align:center;text-transform:uppercase;font-weight:400}
.rule{width:46px;height:2px;background:#c9ccd0;margin:0 auto}

/* hero */
.hero{height:570px;overflow:hidden}
.hero-visual{position:absolute;inset:0;background:
  radial-gradient(ellipse 420px 200px at 50% 62%,rgba(90,150,255,.55),transparent 70%),
  radial-gradient(ellipse 700px 380px at 50% 45%,#1b3f9a,transparent 75%),
  linear-gradient(180deg,#050d2c 0%,#0b1d5e 45%,#06113a 100%)}
.menu{position:absolute;top:32px;right:84px;width:30px}
.menu span{display:block;height:3px;background:var(--white);margin-bottom:6px}
.wordmark{position:absolute;top:185px;left:0;width:100%;text-align:center;color:var(--white);font-family:"Montserrat",Arial,sans-serif;font-weight:600}
.wordmark .name{font-size:190px;line-height:170px;letter-spacing:-4px}
.wordmark .sub{font-size:33px;letter-spacing:7px;margin-top:24px}
.down{position:absolute;left:570px;top:540px}

/* intro */
.intro{height:284px;text-align:center}
.intro .heading{position:absolute;top:66px;left:255px;width:690px;font-size:19px;line-height:24px}
.intro .rule{position:absolute;top:146px;left:577px}
.intro p{position:absolute;top:166px;left:318px;width:564px;font-size:14px;line-height:20px;color:var(--ink)}

/* reach */
.reach{height:572px;background:var(--band)}
.reach .heading{position:absolute;top:44px;left:0;width:100%;color:var(--white);font-size:24px;line-height:28px}
.reach .rule{position:absolute;top:108px;left:577px;background:rgba(255,255,255,.4)}
.map{position:absolute;left:208px;top:136px;width:924px;height:250px;border-radius:60px;
  background:radial-gradient(ellipse at 40% 55%,rgba(255,255,255,.35),rgba(255,255,255,.08) 70%,transparent 100%)}
.countries{position:absolute;left:478px;top:472px;width:468px;color:var(--white);font-size:11px;font-weight:700;line-height:16px;text-align:center}

/* clients */
.clients{height:439px}
.clients .heading{position:absolute;top:76px;width:100%;font-size:24px}
.client{position:absolute;top:170px;width:180px;text-align:center}
.client .photo{width:162px;height:162px;margin:0 auto;border-radius:50%;border:8px solid #f6f7f9;box-shadow:0 2px 8px rgba(0,0,0,.06);
  background:radial-gradient(circle at 50% 38%,#e8d0bd 0 22%,transparent 23%),linear-gradient(180deg,#f4f6f8 0 55%,#9cc3e6 56%,#7fb0dc 100%)}
.client .who{margin-top:12px;font-size:13px;color:var(--muted)}
.client .role{font-size:9px;color:#a5a9ae;text-transform:uppercase}

/* services */
.services{height:415px;background:var(--light)}
.services .heading{position:absolute;top:55px;width:100%;font-size:24px}
.services .lead{position:absolute;top:86px;width:100%;text-align:center;font-size:14px}
.service{position:absolute;width:200px;margin-left:-100px;text-align:center}
.service svg{display:block;margin:0 auto 8px}
.service span{font-family:"Questrial",Arial,sans-serif;font-size:13px;color:#3e4348;text-transform:uppercase}

/* join */
.join{height:432px}
.join .heading{position:absolute;top:66px;width:100%;font-size:24px}
.field{position:absolute;top:132px;height:46px;background:var(--field);font-size:12px;color:#8b9095;padding:15px 20px;text-transform:uppercase;letter-spacing:.5px}
.upload{position:absolute;left:164px;top:183px;width:874px;height:122px;background:var(--field);text-align:center;padding-top:22px;color:#8b9095;font-family:"Questrial",Arial,sans-serif;font-size:17px}
.button{position:absolute;left:503px;width:194px;height:51px;background:var(--brand);color:var(--white);border-radius:3px;box-shadow:0 2px 0 var(--brand-dark);
  font-family:"Questrial",Arial,sans-serif;font-size:16px;text-transform:uppercase;text-align:center;line-height:51px}
.join .button{top:330px}

/* contact */
.contact{height:411px;background:radial-gradient(ellipse at 50% 40%,#16181d,var(--night) 70%)}
.contact .heading{position:absolute;top:78px;width:100%;font-size:24px;color:#2f77c4}
.contact .rule{position:absolute;top:118px;left:577px;background:#3c4048}
.address{position:absolute;top:148px;width:100%;text-align:center;font-family:"Questrial",Arial,sans-serif;font-size:28px;color:#a9adb3;letter-spacing:1px}
.lines{position:absolute;top:202px;width:100%;text-align:center;font-family:"Questrial",Arial,sans-serif;font-size:19px;color:#a9adb3}
.lines span{margin:0 22px}
.lines svg{vertical-align:-3px;margin-right:6px}
.contact .button{top:279px}

.footer{height:108px;text-align:center;padding-top:43px;font-size:14px;color:#555}
</style>
</head>
<body>

<header class="hero">
  <div class="hero-visual" role="img" aria-label="Dark blue digital data centre with glowing circular rings"></div>
  <div class="menu"><span></span><span></span><span></span></div>
  <div class="wordmark">
    <div class="name">Verin</div>
    <div class="sub">GLOBAL SERVICES</div>
  </div>
  <svg class="down" width="60" height="16" viewBox="0 0 60 16"><path d="M2 3 L30 13 L58 3" fill="none" stroke="#fff" stroke-width="3"/></svg>
</header>

<section class="intro">
  <h1 class="heading">Provides security services of various types in challenging or high threat environments internationally for government and private sector organizations.</h1>
  <div class="rule"></div>
  <p>We provide risk assessments, security audits and training, medical support, close protection for individuals, groups and events, crisis management, and evacuation coordination; we enable businesses to operate in challenging locations.</p>
</section>

<section class="reach">
  <h2 class="heading">Our experts are highly trained and qualified with<br>exceptional experience worldwide.</h2>
  <div class="rule"></div>
  <div class="map" role="img" aria-label="Dotted world map with the countries of operation highlighted"></div>
  <p class="countries">USA, CANADA, UK, FRANCE, BOSNIA, UAE, QATAR, LIBYA, TUNISIA, AFGHANISTAN, IRAQ, TURKEY, SUDAN, EGYPT, CENTRAL AFRICAN REPUBLIC, SOMALIA, RWANDA, SOMALILAND.</p>
</section>

<section class="clients">
  <h2 class="heading">Our Clients</h2>
  <div class="client" style="left:110px"><div class="photo" role="img" aria-label="Client portrait"></div><div class="who">John Doe</div><div class="role">CEO</div></div>
  <div class="client" style="left:307px"><div class="photo" role="img" aria-label="Client portrait"></div><div class="who">John Doe</div><div class="role">CEO</div></div>
  <div class="client" style="left:522px;top:164px"><div class="photo" role="img" aria-label="Client portrait"></div><div class="who">John Doe</div><div class="role">CEO</div></div>
  <div class="client" style="left:715px"><div class="photo" role="img" aria-label="Client portrait"></div><div class="who">John Doe</div><div class="role">CEO</div></div>
  <div class="client" style="left:910px"><div class="photo" role="img" aria-label="Client portrait"></div><div class="who">John Doe</div><div class="role">CEO</div></div>
</section>

<section class="services">
  <h2 class="heading">Our Services</h2>
  <p class="lead">We enable businesses to operate in challenging locations.</p>

  <div class="service" style="left:277px;top:152px">
    <svg width="56" height="56" viewBox="0 0 56 56"><path d="M6 26 A22 22 0 0 1 50 26 Z" fill="#15508a"/><line x1="28" y1="26" x2="28" y2="46" stroke="#15508a" stroke-width="3"/><rect x="8" y="30" width="34" height="18" rx="3" fill="#fff" stroke="#15508a" stroke-width="2.5"/><text x="25" y="44" font-family="Open Sans,sans-serif" font-size="11" font-weight="700" fill="#15508a" text-anchor="middle">RISK</text></svg>
    <span>Risk Assessments</span>
  </div>
  <div class="service" style="left:485px;top:152px">
    <svg width="56" height="56" viewBox="0 0 56 56"><rect x="6" y="14" width="34" height="34" rx="2" fill="none" stroke="#15508a" stroke-width="3"/><text x="15" y="34" font-family="Open Sans,sans-serif" font-size="14" font-weight="700" fill="#15508a">$</text><line x1="23" y1="26" x2="35" y2="26" stroke="#15508a" stroke-width="2.5"/><line x1="12" y1="40" x2="35" y2="40" stroke="#15508a" stroke-width="2.5"/><rect x="36" y="10" width="16" height="14" rx="2" fill="#15508a"/><path d="M39 10 V6 A5 5 0 0 1 49 6 V10" fill="none" stroke="#15508a" stroke-width="2.5"/></svg>
    <span>Security Audits</span>
  </div>
  <div class="service" style="left:706px;top:152px">
    <svg width="56" height="56" viewBox="0 0 56 56"><circle cx="24" cy="16" r="9" fill="#15508a"/><path d="M8 52 V40 A14 12 0 0 1 40 40 V52 Z" fill="#15508a"/><path d="M44 4 V16 M38 10 H50" stroke="#15508a" stroke-width="3"/><path d="M20 32 L24 40 L28 32" fill="#fff"/></svg>
    <span>Medical Support</span>
  </div>
  <div class="service" style="left:928px;top:152px">
    <svg width="56" height="56" viewBox="0 0 56 56"><rect x="8" y="6" width="40" height="28" rx="2" fill="none" stroke="#15508a" stroke-width="3"/><rect x="14" y="12" width="12" height="8" fill="#15508a"/><line x1="30" y1="16" x2="42" y2="16" stroke="#15508a" stroke-width="2"/><circle cx="16" cy="42" r="4" fill="#15508a"/><circle cx="28" cy="42" r="4" fill="#15508a"/><circle cx="40" cy="42" r="4" fill="#15508a"/><path d="M10 52 a6 5 0 0 1 12 0 M22 52 a6 5 0 0 1 12 0 M34 52 a6 5 0 0 1 12 0" fill="#15508a"/></svg>
    <span>Training</span>
  </div>
  <div class="service" style="left:478px;top:272px">
    <svg width="56" height="56" viewBox="0 0 56 56"><circle cx="24" cy="16" r="9" fill="#15508a"/><path d="M8 50 V40 A14 12 0 0 1 36 36 L36 50 Z" fill="#15508a"/><circle cx="40" cy="42" r="9" fill="#fff" stroke="#15508a" stroke-width="3"/><path d="M40 37 V42 L44 44" stroke="#15508a" stroke-width="2" fill="none"/></svg>
    <span>Crisis Management</span>
  </div>
  <div class="service" style="left:706px;top:272px">
    <svg width="56" height="56" viewBox="0 0 56 56"><circle cx="38" cy="8" r="5" fill="#15508a"/><path d="M28 16 L40 18 L36 30 L44 38 L40 50 M36 30 L26 38 L18 36 M32 20 L24 26" stroke="#15508a" stroke-width="4" fill="none" stroke-linecap="round"/><line x1="4" y1="24" x2="18" y2="24" stroke="#15508a" stroke-width="2.5"/><line x1="2" y1="32" x2="16" y2="32" stroke="#15508a" stroke-width="2.5"/><line x1="6" y1="40" x2="14" y2="40" stroke="#15508a" stroke-width="2.5"/></svg>
    <span>Evacuation Coordination</span>
  </div>
</section>

<section class="join">
  <h2 class="heading">Join Our Team</h2>
  <div class="field" style="left:164px;width:286px">Name</div>
  <div class="field" style="left:457px;width:286px">Telephone</div>
  <div class="field" style="left:750px;width:288px">Email</div>
  <div class="upload">
    <svg width="80" height="56" viewBox="0 0 80 56"><path d="M22 46 H16 A14 14 0 0 1 18 18 A20 20 0 0 1 56 14 A14 14 0 0 1 62 46 H56" fill="none" stroke="#9a9ea3" stroke-width="3.5"/><path d="M40 54 V24 M30 33 L40 23 L50 33" fill="none" stroke="#9a9ea3" stroke-width="3.5"/></svg>
    <div>UPLOAD YOUR C.V</div>
  </div>
  <div class="button">Join Team</div>
</section>

<section class="contact">
  <h2 class="heading">Have Any Questions?</h2>
  <div class="rule"></div>
  <p class="address">123 , Address abc , City, USA</p>
  <p class="lines">
    <span><svg width="18" height="18" viewBox="0 0 18 18"><path d="M4 1 L7 5 L5 7 A10 10 0 0 0 11 13 L13 11 L17 14 L15 17 A14 14 0 0 1 1 3 Z" fill="none" stroke="#3a86d6" stroke-width="1.6"/></svg>11 22 33 44 55</span>
    <span><svg width="22" height="16" viewBox="0 0 22 16"><rect x="1" y="1" width="20" height="14" fill="none" stroke="#3a86d6" stroke-width="1.6"/><path d="M1 1 L11 9 L21 1" fill="none" stroke="#3a86d6" stroke-width="1.6"/></svg>info@verin.example</span>
  </p>
  <div class="button">Submit Enquiry</div>
</section>

<footer class="footer">Copyright 2015. All Rights Reserved.</footer>

</body>
</html>
```